Website & Logo The full package New Business new design and idea

Word Press

Simple, clean and very professional and approachable if possible

I am looking for a full business concept from logo to colour pallet and everything in between.
Brand new business concept, the successful applicant may continue on as our outsourced point person for all future work.

I will have an animated explainer video going over the four keys to business success Staff, Product & Services, Marketing, Sales and why the need a coach just like a sporting team to stay focused and clear on measurable outcomes.

Just added script (pdf attachment) i will be using for the explainer video at top of site.

Target Market(s)

Small business owners in Australia

Industry/Entity Type

Business Consultant

Number of Pages Required

1 page

Font styles to use
Sans Serif

Colors

Requirements
Must have
• Word press using Divi platform
• Ball park as per pdf uploaded
• Must work on all devices
• Social links
• Clear and straight forward movement through site
• Great capture of name and email,
• Free Download
• 10 Things you can start today in your small business to get you going again!
Nice to have
• clean one page potentially
• Free files and resources page
Should not have
• boring old menu and old framing

```html
<!DOCTYPE html>
<html lang="en">
<head>
<meta charset="utf-8">
<title>Outback Business Coach</title>
<link rel="stylesheet" href="https://fonts.googleapis.com/css2?family=Open+Sans:wght@400;600;700;800&display=swap">
<style>
:root{
  --blue:#2457c5;
  --blue-deep:#1a49b3;
  --blue-btn:#1b4fb6;
  --sky:#1ea0dc;
  --teal:#1b8fc2;
  --teal-deep:#1577ad;
  --bg-light:#eaf5fd;
  --white:#ffffff;
  --ink:#2b2f3a;
  --muted:#7c8594;
  --title-blue:#1f56c0;
}
*{box-sizing:border-box;margin:0;padding:0}
html,body{width:1200px;height:5094px;overflow:hidden}
body{position:relative;font-family:"Open Sans",Arial,sans-serif;color:var(--ink);background:var(--bg-light)}
.backdrop{position:absolute;left:0;top:0}
.abs{position:absolute}
/* header */
.brand{left:112px;top:46px;font-weight:800;font-size:25px;color:var(--white);letter-spacing:-.3px}
.nav{top:56px;left:523px;display:flex;gap:34px;font-size:13px;color:var(--white)}
.btn-outline{left:842px;top:49px;width:94px;height:32px;background:var(--white);color:var(--blue-deep);font-size:10.5px;font-weight:700;display:flex;align-items:center;justify-content:center}
.btn-solid{left:960px;top:49px;width:128px;height:32px;background:var(--blue-btn);color:var(--white);font-size:10.5px;font-weight:700;display:flex;align-items:center;justify-content:center;border:1px solid #fff}
.hero-title{left:110px;top:242px;font-size:39px;font-weight:400;color:var(--white)}
.hero-text{left:112px;top:314px;width:470px;font-size:12.5px;line-height:27px;color:var(--white)}
.signup{left:112px;top:398px;display:flex}
.signup .field{width:326px;height:42px;background:var(--white);font-size:12px;color:#666;padding:13px 20px}
.signup .go{margin-left:12px;width:120px;height:42px;background:var(--sky);color:var(--white);font-weight:700;font-size:15px;display:flex;align-items:center;justify-content:center}
.hero-video{left:648px;top:170px;width:440px;height:308px;border-radius:30px;background:linear-gradient(135deg,#c9d6e6,#8fa4bf 60%,#6e85a4);overflow:hidden}
/* intro */
.intro{left:220px;top:668px;width:760px;text-align:center;font-size:12.8px;line-height:39px;color:#3a3f4b}
/* snapshot */
.snap-title{left:112px;top:1200px;font-size:20px;color:var(--ink)}
.snap-title b{color:var(--title-blue);font-weight:400}
.snap-text{left:112px;top:1245px;width:520px;font-size:11.5px;line-height:30px;color:var(--muted)}
.ticks{left:112px;top:1380px;list-style:none;font-size:13px;color:#2f3440}
.ticks li{height:39px;display:flex;align-items:flex-start;gap:22px}
.dot{width:12px;height:12px;border-radius:50%;background:var(--blue-deep);flex:none;margin-top:3px;position:relative}
.dot::after{content:"";position:absolute;left:4px;top:3px;border-left:4px solid #fff;border-top:3px solid transparent;border-bottom:3px solid transparent}
.snap-ring{left:695px;top:1180px;width:420px;height:420px;border-radius:50%;background:var(--white);box-shadow:0 10px 40px rgba(40,80,140,.15)}
.snap-art{left:747px;top:1227px;width:316px;height:316px;border-radius:50%;background:radial-gradient(circle at 40% 35%,#2fa3e8,#1c5fc7 60%,#1546a8)}
/* cards */
.card{top:1858px;width:306px;height:400px;background:var(--white);border-radius:20px;box-shadow:0 8px 24px rgba(40,80,140,.1);text-align:center;padding-top:36px}
.card svg{display:block;margin:0 auto}
.card h3{font-size:13.5px;font-weight:600;line-height:22px;margin-top:18px;color:#2b2f3a}
.card p{font-size:10.6px;line-height:27px;color:var(--muted);padding:0 26px;margin-top:12px}
.card .more{position:absolute;left:90px;bottom:-18px;width:126px;height:36px;background:var(--blue-btn);color:var(--white);font-size:10.5px;font-weight:700;display:flex;align-items:center;justify-content:center}
/* how it works */
.how-art{left:110px;top:2590px;width:410px;height:400px;border-radius:50% 50% 46% 46%;background:radial-gradient(ellipse at 50% 70%,#cfeef7,#e8dcf1 55%,#ffffff 80%)}
.how-title{left:604px;top:2624px;font-size:30px;font-weight:400;color:var(--ink)}
.how-text{left:606px;top:2686px;width:460px;font-size:12px;line-height:34px;color:var(--muted)}
/* activities */
.act-lead{left:112px;top:3176px;width:700px;font-size:12px;line-height:34px;color:var(--white)}
.act-lead b{font-weight:700}
.act-head{left:112px;top:3302px;font-size:16px;color:var(--white)}
.act-list{list-style:none;font-size:10.5px;color:var(--white)}
.act-list li{display:flex;gap:14px;height:34px;line-height:17px}
.act-list .dot{background:var(--white);width:11px;height:11px}
.act-list .dot::after{border-left-color:var(--teal)}
/* application */
.app-title{left:112px;top:3798px;font-size:32px;font-weight:400;color:var(--ink)}
.app-text{left:112px;top:3868px;width:450px;font-size:12px;line-height:34px;color:var(--muted)}
.app-btn{left:112px;top:4072px;width:238px;height:50px;background:var(--blue-btn);color:var(--white);font-size:14px;font-weight:700;display:flex;align-items:center;justify-content:center;gap:8px}
.app-art{left:625px;top:3735px;width:465px;height:450px;border-radius:44% 56% 50% 50%;background:linear-gradient(160deg,#dfe9f6,#c9d9ef 60%,#eef3fa)}
/* about */
.about-title{left:488px;top:4452px;font-size:40px;font-weight:400;color:var(--white)}
.about-text{left:488px;top:4522px;width:570px;font-size:11.5px;line-height:37px;color:var(--white)}
.cta{left:488px;top:4800px;width:420px;height:72px;background:var(--white);display:flex;align-items:center;gap:16px;padding-left:16px}
.cta .icon{width:40px;height:40px;border-radius:50%;background:var(--blue-btn);display:flex;align-items:center;justify-content:center;flex:none}
.cta span{font-size:11.5px;font-weight:700;line-height:24px;color:var(--blue-deep)}
/* footer */
.copy{left:0;width:1200px;top:5000px;text-align:center;font-size:13px;color:#2f3440}
.social{left:536px;top:5050px;display:flex;gap:18px}
.social i{width:18px;height:18px;border-radius:50%;background:#1f2430;display:block}
.chat{left:1042px;top:5017px;width:46px;height:46px;border-radius:50%;background:var(--blue-deep);display:flex;align-items:center;justify-content:center}
</style>
</head>
<body>

<svg class="backdrop" width="1200" height="5094" viewBox="0 0 1200 5094" aria-hidden="true">
  <defs>
    <linearGradient id="heroGrad" x1="0" y1="0" x2="1" y2="1">
      <stop offset="0" stop-color="#2a5fc9"/><stop offset="1" stop-color="#1d4cb8"/>
    </linearGradient>
    <linearGradient id="tealGrad" x1="0" y1="0" x2="1" y2="0">
      <stop offset="0" stop-color="#1c94c6"/><stop offset="1" stop-color="#137bb0"/>
    </linearGradient>
    <linearGradient id="aboutGrad" x1="0" y1="0" x2="1" y2="1">
      <stop offset="0" stop-color="#2458c4"/><stop offset="1" stop-color="#1846ad"/>
    </linearGradient>
  </defs>
  <rect width="1200" height="5094" fill="#eaf5fd"/>
  <path d="M0 0H868C830 110 805 250 720 390C640 520 450 560 0 632Z" fill="url(#heroGrad)"/>
  <!-- snapshot band -->
  <path d="M0 1150C300 1110 580 1000 800 1006C1000 1012 1110 1110 1200 1160V1650C1080 1710 880 1770 620 1752C360 1734 180 1610 0 1612Z" fill="#fff"/>
  <path d="M0 1150C220 1128 420 1080 560 1040" fill="none" stroke="#2457c5" stroke-width="5"/>
  <!-- how it works band -->
  <path d="M0 2530C300 2490 600 2380 800 2380C1000 2380 1100 2440 1200 2460V3100H0Z" fill="#fff"/>
  <path d="M0 2530C220 2508 420 2465 540 2430" fill="none" stroke="#2457c5" stroke-width="5"/>
  <rect x="0" y="3300" width="1200" height="1794" fill="#fff"/>
  <!-- activities band -->
  <path d="M0 3130C400 3090 800 3010 1200 2935V3535C900 3600 500 3625 0 3545Z" fill="url(#tealGrad)"/>
  <!-- about band -->
  <path d="M1200 4310C950 4360 560 4410 360 4470C180 4530 130 4700 150 4860C170 4985 300 4995 520 4970C820 4940 1090 4905 1200 4875Z" fill="url(#aboutGrad)"/>
</svg>

<!-- header -->
<div class="abs brand">OUTBACK BUSINESS COACH</div>
<nav class="abs nav"><span>Home</span><span>About us</span><span>How it all works</span></nav>
<div class="abs btn-outline">CONTACT US</div>
<div class="abs btn-solid">FREE DOWNLOAD</div>

<h1 class="abs hero-title">Outback Business Coach</h1>
<p class="abs hero-text">Sed ut perspiciatis unde omnis iste natus error sit voluptatem accusantium doloremque laudantium totam rem aperiameaque ipsa quae</p>
<div class="abs signup"><div class="field">Email Address</div><div class="go">SIGN UP</div></div>
<div class="abs hero-video" role="img" aria-label="Explainer video still: coach and client working together at a laptop, with play button">
  <svg width="440" height="308" viewBox="0 0 440 308"><circle cx="220" cy="154" r="34" fill="none" stroke="#fff" stroke-width="5"/><path d="M210 136L238 154L210 172Z" fill="#fff"/></svg>
</div>

<div class="abs intro">
Outback Business Coach is here to help, support and turn your small business around, It may not be easy, it may not be pretty, it may not be conventional or what you want to hear but my only goal is to help you succeed in your small business struggling in Australia.<br>
I offer a 12 week fully supported and personally applied program, each week you complete the activities and we meet over video call where your actions are accountable and measurable.<br>
Every business and small business owner are different, so not one solution fits all, and that's exactly why I can make it personal for those who want to change and need it to happen now..
</div>

<!-- snapshot -->
<h2 class="abs snap-title"><b>Australian Small Business</b> Snapshot Nov 26, 2018</h2>
<p class="abs snap-text">It's an extremely sad sign of the times when you're confronted with a myriad of 'for lease' signs in shop windows along major shopping hubs.<br>While most businesses in Australia are small -- accounting for 97 percent of all businesses -- they're shutting their doors in alarmingly high numbers.</p>
<ul class="abs ticks">
  <li><span class="dot"></span>What is the Small Business Failure Rate?</li>
  <li><span class="dot"></span>20% of small businesses fail in their first year</li>
  <li><span class="dot"></span>30% of small business fail in their second year</li>
  <li><span class="dot"></span>50% of small businesses fail after five years in business.</li>
  <li><span class="dot"></span>Finally, 70% of small business owners fail in their 10th year in business.</li>
</ul>
<div class="abs snap-ring"></div>
<div class="abs snap-art" role="img" aria-label="Illustration of a team building a rising bar chart together"></div>

<!-- offers -->
<div class="abs card" style="left:112px">
  <svg width="56" height="56" viewBox="0 0 56 56" fill="none" stroke="#1b4fb6" stroke-width="2.5"><circle cx="30" cy="28" r="18"/><path d="M35 21c-2-2-9-2-9 2s9 3 9 7-7 4-9 2M30 16v24M6 30l6-6 6 6"/></svg>
  <h3>Giving Back Free</h3>
  <p>Outback Business Coach is offering 4 FREE 12-week coaching one on one support program every 3 months to struggling businesses in 2019 as our way of giving back and helping others in need, just fill out the information sheet and we will let you know as soon as possible. Maybe show the 12 free placements along</p>
  <div class="more">READ MORE</div>
</div>
<div class="abs card" style="left:448px">
  <svg width="56" height="56" viewBox="0 0 56 56" fill="none" stroke="#1b4fb6" stroke-width="2.5"><path d="M28 6l6 5 8-1 2 8 6 5-4 7 1 8-8 2-5 6-6-4-6 4-5-6-8-2 1-8-4-7 6-5 2-8 8 1z"/><path d="M22 34l12-12"/><circle cx="22" cy="23" r="2.5"/><circle cx="34" cy="33" r="2.5"/></svg>
  <h3>Special Offer -<br>Below Cost Price $200 a<br>week for 12 weeks</h3>
  <p>Outback Business Coach is offering this incredible one on one support program to only 12 small business owners in the first quarter in 2019 at below cost, so if you need help now, just fill out the information sheet and we will let</p>
  <div class="more">READ MORE</div>
</div>
<div class="abs card" style="left:782px">
  <svg width="56" height="56" viewBox="0 0 56 56" fill="none" stroke="#1b4fb6" stroke-width="2.5"><rect x="6" y="10" width="44" height="38"/><path d="M6 20h44M16 6v8M40 6v8M12 27h32M12 34h32M12 41h32M20 24v20M28 24v20M36 24v20"/></svg>
  <h3>Just A Bit More $400 a<br>week for 12 weeks</h3>
  <p>Very limited on application only just 4 clients per quarter, here we provide additional one on one support each week and dive deeper into every element of your business and fast track the changes, just fill out the information sheet and we will let you know as soon as possible.</p>
  <div class="more">READ MORE</div>
</div>

<!-- how it works -->
<div class="abs how-art" role="img" aria-label="Illustration of a person coding at a desk surrounded by floating web technology tiles"></div>
<h2 class="abs how-title">How it all works</h2>
<p class="abs how-text">With your permission I breakdown your business, Staff, Products / Services, Marketing and Sales. Under each of these four key components are up to 30 or more components including your staff training and experience, business financials, public exposure and engagement with target market, current marketing and processes required to make income.</p>

<!-- activities -->
<p class="abs act-lead">Regardless if you're a Outback Business <b>Coach Free, Special Offer or Just a Bit More,</b> Small Business Owner you all get one on one direct access to me each week along with mountains of accountable activities to turn your small business around into the dream you had hoped it could be.</p>
<h3 class="abs act-head">Activates include</h3>
<ul class="abs act-list" style="left:112px;top:3346px">
  <li><span class="dot"></span>Getting a measurable base line of the financials and existing marketing.</li>
  <li><span class="dot"></span>Discussing the past ups and downs and looking forward to the future</li>
  <li><span class="dot"></span>Understanding your product or service and how it fits into the current marketplace.</li>
  <li><span class="dot"></span>Looking into the staff for potential opportunities or training.</li>
  <li><span class="dot"></span>Understanding market trends and embracing a SWOT analysis</li>
</ul>
<ul class="abs act-list" style="left:634px;top:3312px;width:460px">
  <li><span class="dot"></span>Looking to establish a mastermind local group with a successful business</li>
  <li><span class="dot"></span>Partnership opportunities</li>
  <li><span class="dot"></span>Creating and applying marketing objectives</li>
  <li><span class="dot"></span>How to give more to grow</li>
  <li style="height:auto"><span class="dot"></span>External learning materials applied as per needs such as specific podcast episodes or suggested books that relate to a special need to be supported.</li>
</ul>

<!-- application -->
<h2 class="abs app-title">Application</h2>
<p class="abs app-text">Placements are strictly limited to 28 per quarter as they are all managed personally for the best possible outcomes.<br>You must have internet access, put the time aside between 1-2 hours a week on video call and be open to change and motivated and accountable to succeed with every scheduled meeting.</p>
<div class="abs app-btn"><svg width="14" height="14" viewBox="0 0 14 14" fill="#fff"><path d="M5 0h4v6h3L7 11 2 6h3zM0 12h14v2H0z"/></svg>FREE DOWNLOAD</div>
<div class="abs app-art" role="img" aria-label="Illustration of a businessman seated inside a large phone screen among leafy plants"></div>

<!-- about -->
<h2 class="abs about-title">About Me</h2>
<p class="abs about-text">I am not superman, I just found myself absorbing information over the past 10 years through some mentors and personal development and see so many small business owners struggling and I got sick of telling myself how I would change things that I eventually approached some businesses for free and asked if they needed a hand and they were over the moon, very receptive and after a 1 hour talk the immediate action taken saw some massive returns exceeding even my estimates and now I just want to help more Small Business Owners through Outback Business Coach support.</p>
<div class="abs cta">
  <div class="icon"><svg width="20" height="20" viewBox="0 0 20 20" fill="none" stroke="#fff" stroke-width="2.5"><path d="M3 10h13M11 5l5 5-5 5"/></svg></div>
  <span>10 THINGS YOU CAN START TODAY IN<br>YOUR SMALL BUSINESS TO GET YOU GOING AGAIN!</span>
</div>

<!-- footer -->
<p class="abs copy">Copyright 2018 Outback Business Coach &nbsp;|&nbsp; Terms &amp; Privacy</p>
<div class="abs social" aria-label="Social links"><i></i><i></i><i></i><i></i></div>
<div class="abs chat" aria-label="Chat">
  <svg width="24" height="20" viewBox="0 0 24 20"><path d="M2 2h20v12H9l-5 4v-4H2z" fill="#fff"/><circle cx="8" cy="8" r="1.5" fill="#1a49b3"/><circle cx="12" cy="8" r="1.5" fill="#1a49b3"/><circle cx="16" cy="8" r="1.5" fill="#1a49b3"/></svg>
</div>

</body>
</html>
```